Revamp my web site design

Willowbrook Care Practitioners is a not for profit organisation focused on providing emotional support and counselling services to those with cancer or affected by cancer including those bereaved.

Our web site is intended to welcome suffers to engage with the services of its members and is also provided to encourage additional counsellors to join the organisation and then supports its members with access to materials and courses to extend their professional development.

We have a limited budget and seek to not only improve the attractiveness of the site but also improve the functionality and ease of maintenance. Especially site administrtaion should allow for uploading documents, adding new members, news and events easily.

Existing site is www.willowbrookcare.com.au

```html
<!DOCTYPE html>
<html lang="en">
<head>
<meta charset="utf-8">
<title>Willowbrook Care Practitioners</title>
<link href="https://fonts.googleapis.com/css2?family=Mulish:wght@300;400;600&display=swap" rel="stylesheet">
<style>
:root{
  --green:#4fa800;
  --green-text:#4a9e00;
  --ink:#2e2e2e;
  --body:#4a4a4a;
  --muted:#8f8f8f;
  --bg-top:#f2f2f2;
  --bg-light:#f8f8f8;
  --bg-mid:#f1f1f1;
  --bg-foot:#eaeaea;
  --rule:#bdbdbd;
  --cream:#fbeedc;
  --orange:#f08a1c;
  --button:#3e3e3e;
}
*{box-sizing:border-box;margin:0;padding:0}
html,body{width:988px;height:1200px;overflow:hidden}
body{position:relative;font-family:"Mulish",sans-serif;color:var(--body);background:var(--bg-mid);letter-spacing:.3px}
.abs{position:absolute}
.band-top{left:0;top:0;width:988px;height:388px;background:var(--bg-top)}
.band-welcome{left:0;top:388px;width:988px;height:253px;background:var(--bg-light)}
.band-foot{left:0;top:1120px;width:988px;height:80px;background:var(--bg-foot)}

.brand{left:105px;top:32px;display:flex;flex-direction:column;align-items:flex-start;gap:12px}
.brand-mark{width:56px;height:56px;border-radius:50%;background:var(--green);margin-left:36px}
.brand-name{font-size:16px;font-weight:600;color:var(--ink);letter-spacing:0}

.search{left:682px;top:49px;width:203px;height:22px;background:#e9e9e9;border-radius:2px;font-size:7px;color:#a8a8a8;padding:6px 7px}
.search svg{position:absolute;right:6px;top:5px}

.nav{right:103px;top:102px;display:flex;gap:17px;font-size:12px;color:var(--ink);letter-spacing:.2px}
.nav .active{color:var(--green-text)}

.hero{left:103px;top:134px;width:781px;height:337px;background:var(--cream);overflow:hidden}
.hero-photo{left:0;top:0;width:300px;height:337px;background:linear-gradient(90deg,#8a5a3a 0%,#b88762 45%,#e6c9a6 80%,#fbeedc 100%)}
.hero-title{left:275px;top:130px;font-size:43px;font-weight:400;line-height:41px;letter-spacing:.5px}
.hero-title .l1{color:var(--green);display:block}
.hero-title .l2{color:var(--ink);display:block}
.dots{left:366px;top:304px;display:flex;gap:3px}
.dots span{width:10px;height:10px;border-radius:50%;background:#3a3a3a}
.dots span.on{background:transparent;border:1.5px solid #3a3a3a}

.finder{left:545px;top:32px;width:220px;height:264px;background:var(--green);border-radius:6px;padding:16px 14px;color:#fff}
.finder h2{font-size:21px;font-weight:400;letter-spacing:.5px}
.finder p{font-size:13px;margin:9px 0 9px}
.field{width:190px;height:28px;background:#fff;margin:0 0 12px 1px;font-size:9px;color:#a9a9a9;padding:8px 7px}
.finder .btn{position:absolute;left:59px;top:204px;width:102px;height:33px;background:var(--button);color:#fff;font-size:16px;text-align:center;line-height:33px}

.welcome{left:90px;top:498px;width:808px;text-align:center}
.welcome h1{font-size:16px;font-weight:400;color:var(--green-text);margin-bottom:14px;letter-spacing:.4px}
.welcome p{font-size:11.5px;line-height:22.5px;color:var(--body);letter-spacing:.55px}

.col h3{font-size:15px;font-weight:400;color:var(--ink);padding:0 0 8px 1px;border-bottom:1px solid var(--rule)}
.news{left:103px;top:688px;width:222px}
.date{font-size:9.5px;color:var(--muted);margin-top:9px}
.item{display:flex;gap:11px;margin-top:10px}
.thumb{width:90px;height:74px;flex:none;background:linear-gradient(135deg,#e7eef3,#b8c7d3 60%,#f4f4f4)}
.item-title{font-size:11.5px;line-height:17.5px;color:var(--ink);margin-top:-1px}
.excerpt{font-size:11.5px;line-height:19.7px;color:var(--muted);text-align:justify;margin-top:12px}
.excerpt a{color:var(--green-text);text-decoration:none}

.events{left:366px;top:688px;width:222px}
.event{position:relative;padding-left:27px}
.event .ico{position:absolute;left:-2px;top:0}
.event .t{font-size:12px;color:var(--green-text)}
.event .d{font-size:9.5px;color:var(--ink);margin-top:6px}

.articles{left:630px;top:688px;width:255px}
.art-img{width:254px;height:110px;margin-top:24px;background:linear-gradient(180deg,#e89a6a 0%,#f6b04a 45%,#c0507a 80%,#7a2c55 100%)}
.articles h4{font-size:15px;font-weight:400;color:var(--ink);line-height:21px;margin-top:16px;width:235px}
.articles p{font-size:11.5px;line-height:20.6px;color:var(--body);margin-top:13px;width:250px;letter-spacing:.45px}

.foot-nav{left:104px;top:1143px;display:flex;gap:17px;font-size:12px;color:var(--ink)}
.copy{left:102px;top:1168px;font-size:11.5px;color:var(--body)}
.social{left:761px;top:1148px;display:flex;gap:5px}
.social span{width:34px;height:34px;border-radius:50%;background:var(--orange)}
</style>
</head>
<body>
<div class="abs band-top"></div>
<div class="abs band-welcome"></div>
<div class="abs band-foot"></div>

<div class="abs brand"><span class="brand-mark"></span><span class="brand-name">Willowbrook Care</span></div>

<div class="abs search">Type search
  <svg width="10" height="10" viewBox="0 0 10 10"><circle cx="4" cy="4" r="3" fill="none" stroke="#999" stroke-width="1.2"/><line x1="6.2" y1="6.2" x2="9.3" y2="9.3" stroke="#999" stroke-width="1.4"/></svg>
</div>

<nav class="abs nav"><span class="active">Home</span><span>News</span><span>Events</span><span>Articles</span><span>Find a Counsellor</span><span>Members</span><span>Contact Us</span></nav>

<section class="abs hero">
  <div class="abs hero-photo" role="img" aria-label="Photo of a smiling older couple embracing"></div>
  <div class="abs hero-title"><span class="l1">Cancer</span><span class="l2">Counseling</span></div>
  <div class="abs dots"><span class="on"></span><span></span><span></span><span></span></div>
  <form class="abs finder">
    <h2>Find A Counseller</h2>
    <p>Search by</p>
    <div class="field">Location</div>
    <div class="field">Last Name</div>
    <div class="field">Counselling Method</div>
    <div class="btn">Search</div>
  </form>
</section>

<section class="abs welcome">
  <h1>Welcome to Willowbrook Care Practitioners&nbsp; Inc</h1>
  <p>A diagnosis of cancer is a devastating experience for most people.<br>
  Many people can get support by talking to close family or friends. However, it can sometimes help to talk to someone from outside of<br>
  that circle who has been trained to listen and help you explore your feelings.&nbsp; You may feel as if you are riding an emotional<br>
  rollercoaster. Often talking of your distress to those close to you can be difficult and painful.</p>
</section>

<section class="abs col news">
  <h3>News</h3>
  <div class="date">June 24, 2013</div>
  <div class="item"><div class="thumb" role="img" aria-label="Photo of a doctor with two nurses"></div><div class="item-title">Kidney cancer progression linked to shifts in tumor metabolism;</div></div>
  <p class="excerpt">Investigators in The Tumour Mapping Research Network have uncovered a connection ...<a href="#">Read More</a></p>
  <div class="date" style="margin-top:18px">June 24, 2013</div>
  <div class="item"><div class="thumb" role="img" aria-label="Photo of a consultation handshake at a desk"></div><div class="item-title">Kidney cancer progression linked to shifts in tumor metabolism;</div></div>
  <p class="excerpt">Investigators in The Tumour Mapping Research Network have uncovered a connection ...<a href="#">Read More</a></p>
</section>

<section class="abs col events">
  <h3>Events</h3>
  <div style="height:32px"></div>
  <div class="event"><svg class="ico" width="17" height="17" viewBox="0 0 17 17"><circle cx="8.5" cy="8.5" r="8.5" fill="#5a5a5a"/><path d="M7 5l3.5 3.5L7 12" fill="none" stroke="#fff" stroke-width="1.8"/></svg><div class="t">Participate in an Event</div><div class="d">May 2013 ,22nd GST 22:10</div></div>
  <div style="height:46px"></div>
  <div class="event"><svg class="ico" width="17" height="17" viewBox="0 0 17 17"><circle cx="8.5" cy="8.5" r="8.5" fill="#5a5a5a"/><path d="M7 5l3.5 3.5L7 12" fill="none" stroke="#fff" stroke-width="1.8"/></svg><div class="t">Gather.Honour.Stand Together</div><div class="d">May 2013 ,22nd GST 22:10</div></div>
  <div style="height:46px"></div>
  <div class="event"><svg class="ico" width="17" height="17" viewBox="0 0 17 17"><circle cx="8.5" cy="8.5" r="8.5" fill="#5a5a5a"/><path d="M7 5l3.5 3.5L7 12" fill="none" stroke="#fff" stroke-width="1.8"/></svg><div class="t">&nbsp;What is Walk For Hope?</div><div class="d">May 2013 ,22nd GST 22:10</div></div>
  <div style="height:40px"></div>
  <div class="event"><svg class="ico" width="17" height="17" viewBox="0 0 17 17"><circle cx="8.5" cy="8.5" r="8.5" fill="#5a5a5a"/><path d="M7 5l3.5 3.5L7 12" fill="none" stroke="#fff" stroke-width="1.8"/></svg><div class="t">History of Walk For Hope</div><div class="d">May 2013 ,22nd GST 22:10</div></div>
  <div style="height:31px"></div>
  <div class="event"><svg class="ico" width="17" height="17" viewBox="0 0 17 17"><circle cx="8.5" cy="8.5" r="8.5" fill="#5a5a5a"/><path d="M7 5l3.5 3.5L7 12" fill="none" stroke="#fff" stroke-width="1.8"/></svg><div class="t">How Donations Save Lives</div><div class="d">May 2013 ,22nd GST 22:10</div></div>
</section>

<section class="abs col articles">
  <h3>Articles</h3>
  <div class="art-img" role="img" aria-label="Photo of a person meditating on a mountain at sunset"></div>
  <h4>Sed ut perspiciatis unde omnis iste natus error sit voluptatem accusantium</h4>
  <p>Doloremque laudantium, totam rem aperiam, eaque ipsa quae ab illo inventore veritatis et quasi architecto beatae vitae dicta sunt explicabo. Nemo enim ipsam voluptatem quia voluptas sit aspernatur aut odit aut fugit, sed quia consequuntur magni dolores eos qui ratione voluptatem .</p>
</section>

<nav class="abs foot-nav"><span>Home</span><span>News</span><span>Events</span><span>Articles</span><span>Find a Counsellor</span><span>Members</span><span>Contact Us</span></nav>
<div class="abs copy">© Company Name. 2013 All Rights Reserved</div>
<div class="abs social" aria-label="Social links"><span></span><span></span><span></span></div>
</body>
</html>
```